Refrigerator Banner

We are purchasing a container of refrigerators. One of our competitors overseas has a really nice sticker/canopy header on top of the light box. please see attched Pic A & Pic B.
Now, we would like to have a sort of similar look and just different enough not to upset anyone. However, this competitor is on the other side of the world, so we don't really compete with each other. So maybe the same blue but have the water thinghy a bit different.
Also, our brand name is "KORVALE Refrigeration"
I would design in the following dimensions:
• 572mm × 223mm
• 1125mm × 223mm
• 1705mm × 223mm
thanks

```html
<!DOCTYPE html>
<html lang="en">
<head>
<meta charset="utf-8">
<title>KORVALE Refrigeration – Canopy Header Sizes</title>
<link rel="stylesheet" href="https://fonts.googleapis.com/css2?family=Tinos:wght@700&family=Dancing+Script:wght@500&display=swap">
<style>
  :root {
    --stage-dark: #555555;
    --stage-light: #ababab;
    --water-deep: #0753c9;
    --water-mid: #0a6be6;
    --water-bright: #1a86f2;
    --water-foam: #8cc4f7;
    --ink-white: #ffffff;
    --label-white: #f4f4f4;
  }
  * { margin: 0; padding: 0; box-sizing: border-box; }
  html, body { width: 1200px; height: 960px; overflow: hidden; }
  body {
    position: relative;
    background: linear-gradient(90deg, var(--stage-dark) 0%, var(--stage-light) 100%);
    font-family: "Tinos", "Times New Roman", serif;
  }
  .banner {
    position: absolute;
    left: 0;
    overflow: hidden;
  }
  .banner--small  { top: 0;     width: 1114px; height: 434px; }
  .banner--medium { top: 469px; width: 1114px; height: 219px; }
  .banner--large  { top: 726px; width: 1200px; height: 156px; }

  .water-photo {
    position: absolute;
    inset: 0;
    background:
      radial-gradient(ellipse 60% 14% at 25% 58%, rgba(200,228,252,0.75), rgba(200,228,252,0) 100%),
      radial-gradient(ellipse 45% 10% at 65% 66%, rgba(140,196,247,0.55), rgba(140,196,247,0) 100%),
      linear-gradient(180deg, var(--water-deep) 0%, var(--water-mid) 40%, var(--water-foam) 58%, var(--water-bright) 66%, var(--water-mid) 100%);
  }
  .banner--medium .water-photo,
  .banner--large .water-photo {
    background:
      radial-gradient(ellipse 60% 22% at 22% 48%, rgba(200,228,252,0.75), rgba(200,228,252,0) 100%),
      radial-gradient(ellipse 45% 16% at 65% 68%, rgba(140,196,247,0.55), rgba(140,196,247,0) 100%),
      linear-gradient(180deg, var(--water-mid) 0%, var(--water-foam) 45%, var(--water-bright) 65%, var(--water-mid) 100%);
  }

  .brand {
    position: absolute;
    text-align: right;
    color: var(--ink-white);
    line-height: 1;
  }
  .brand__name {
    display: block;
    font-family: "Tinos", "Times New Roman", serif;
    font-weight: 700;
    letter-spacing: 0.5px;
  }
  .brand__tagline {
    display: block;
    font-family: "Dancing Script", cursive;
    font-weight: 500;
  }
  .banner--small .brand  { right: 70px; top: 76px; }
  .banner--small .brand__name { font-size: 64px; }
  .banner--small .brand__tagline { font-size: 33px; margin-top: 4px; }

  .banner--medium .brand { right: 58px; top: 36px; }
  .banner--medium .brand__name { font-size: 45px; }
  .banner--medium .brand__tagline { font-size: 23px; margin-top: 2px; }

  .banner--large .brand  { right: 44px; top: 34px; }
  .banner--large .brand__name { font-size: 45px; }
  .banner--large .brand__tagline { font-size: 23px; margin-top: 2px; }

  .size-label {
    position: absolute;
    color: var(--label-white);
    font-family: "Tinos", "Times New Roman", serif;
    font-weight: 700;
    font-size: 32px;
    white-space: nowrap;
  }
  .size-label--vertical {
    transform: translate(-50%, -50%) rotate(-90deg);
  }
  .size-label--small  { left: 1156px; top: 216px; }
  .size-label--medium { left: 1156px; top: 553px; }
  .size-label--large  { left: 598px; top: 920px; transform: translate(-50%, -50%); }
</style>
</head>
<body>
  <section class="banner banner--small">
    <div class="water-photo" role="img" aria-label="Close-up photo of a rippling blue water surface with bubbles"></div>
    <div class="brand">
      <span class="brand__name">KORVALE</span>
      <span class="brand__tagline">Refrigeration</span>
    </div>
  </section>

  <section class="banner banner--medium">
    <div class="water-photo" role="img" aria-label="Close-up photo of a rippling blue water surface with bubbles"></div>
    <div class="brand">
      <span class="brand__name">KORVALE</span>
      <span class="brand__tagline">Refrigeration</span>
    </div>
  </section>

  <section class="banner banner--large">
    <div class="water-photo" role="img" aria-label="Close-up photo of a rippling blue water surface with bubbles"></div>
    <div class="brand">
      <span class="brand__name">KORVALE</span>
      <span class="brand__tagline">Refrigeration</span>
    </div>
  </section>

  <p class="size-label size-label--vertical size-label--small">572mm × 223mm</p>
  <p class="size-label size-label--vertical size-label--medium">1125mm × 223mm</p>
  <p class="size-label size-label--large">1705mm × 223mm</p>
</body>
</html>
```